Mobile version of Desktop site

I need a mobile version of my desktop site. Up until now we have been using a mobile translation service but there are too many drawbacks and bugs. So I need a mobile site designed to be used on an Zephyr or android phone that is "Inspired by" our desktop site. I am going to setup two completely separate sites, served either as desktop or mobile.

I have attached an eps version of my logo.

Design this site as though the largest screen it will be viewed on is an Zephyr 4 max, but more likely it will be viewed on smaller screens.

Phone number as a button to click to call should be prominent.

Just need a basic attorney website that is clean and has the look and feel of the desktop site, but readable and usable on a smartphone.

Base your design off of an inner page like whats on this url:
Desktop url: https://www.brambleworthlegal.com/corvana-heights.html
Updates

Reason: I am extending the deadline to allow for implementation of feedback

Target Market(s)

everyone

Industry/Entity Type

Attorney

Number of Pages Required

1 page

Font styles to use
Sans Serif

Requirements
Must have
• Must be readable and usable on a smart phone, from a 5.5" Zephyr 4 max on down to the original Zephyr. I'm looking for usability and readability.
Nice to have
• I would like to see logos shown at the top filling the width of the page if viewed in portrait mode with the phone number next, and it should be a complementing version of my desktop site.
Should not have
• I do not want to see a lot of small details that would be lost on a smartphone platform.

```html
<!DOCTYPE html>
<html lang="en">
<head>
<meta charset="utf-8">
<title>Brambleworth Attorneys – Mobile</title>
<link rel="stylesheet" href="https://fonts.googleapis.com/css2?family=Open+Sans:wght@300;400;600;700&display=swap">
<style>
  :root{
    --page-bg:#d9dbde;
    --screen-bg:#ffffff;
    --status-bg:#d4d4d4;
    --navy:#1f3d6b;
    --brand-blue:#3a5f8c;
    --phone-blue:#2f5c8f;
    --call-icon:#4ab0e6;
    --text-dark:#333333;
    --text-mid:#555555;
    --line:#e4e4e4;
    --panel-bg:#f6f6f6;
    --caption-bg:rgba(16,52,110,.88);
    --sea-top:#6f9fd6;
    --sea-mid:#8fa6a8;
    --sea-deep:#1d5cb8;
  }
  *{box-sizing:border-box;margin:0;padding:0}
  html,body{width:1154px;height:1200px;overflow:hidden;background:var(--page-bg);font-family:"Open Sans",Arial,sans-serif}
  .screen{position:absolute;left:241px;top:6px;width:672px;height:1188px;background:var(--screen-bg);overflow:hidden;box-shadow:0 4px 24px rgba(0,0,0,.18)}
  .status-bar{position:absolute;left:0;top:0;width:672px;height:40px;background:linear-gradient(#e0e0e0,var(--status-bg));display:flex;align-items:center;padding:0 14px;font-size:24px;color:#222;letter-spacing:-.5px}
  .status-bar .carrier{display:flex;align-items:center;gap:6px}
  .status-bar .dots{display:flex;gap:3px}
  .status-bar .dot{width:11px;height:11px;border-radius:50%;background:#222}
  .status-bar .dot.off{background:none;border:1.5px solid #222}
  .status-bar .time{position:absolute;left:0;right:0;text-align:center;font-weight:700;pointer-events:none}
  .status-bar .battery{margin-left:auto;display:flex;align-items:center;gap:8px}
  .battery-icon{width:50px;height:18px;border:2px solid #222;padding:2px;position:relative}
  .battery-icon::before{content:"";display:block;width:100%;height:100%;background:#222}
  .battery-icon::after{content:"";position:absolute;right:-5px;top:4px;width:3px;height:6px;background:#222}
  .site-header{position:absolute;left:0;top:40px;width:672px;height:117px;border-bottom:2px solid var(--line)}
  .brand{position:absolute;left:38px;top:34px;font-size:36px;font-weight:600;color:var(--navy);letter-spacing:.5px;line-height:1}
  .menu-button{position:absolute;right:0;top:0;width:104px;height:117px;background:var(--brand-blue);display:flex;align-items:center;justify-content:center}
  .call-block{position:absolute;left:0;top:157px;width:672px;height:160px}
  .call-text{position:absolute;right:138px;top:30px;text-align:right;font-size:31px;font-weight:300;color:var(--text-mid);line-height:1}
  .call-text strong{font-weight:700;color:var(--text-dark)}
  .call-number{position:absolute;right:138px;top:84px;font-size:35px;font-weight:700;color:var(--phone-blue);line-height:1;text-decoration:none}
  .call-button{position:absolute;left:565px;top:43px;width:80px;height:80px;border-radius:14px;background:var(--call-icon);display:flex;align-items:center;justify-content:center}
  .hero{position:absolute;left:26px;top:317px;width:620px;height:403px;overflow:hidden}
  .hero-photo{position:absolute;inset:0;background:linear-gradient(180deg,var(--sea-top) 0%,#a8b9c6 14%,var(--sea-mid) 30%,#5f7f9a 45%,var(--sea-deep) 65%,#1a4fa8 100%)}
  .hero-caption{position:absolute;left:0;bottom:0;width:100%;height:75px;background:var(--caption-bg);display:flex;align-items:center;padding:0 27px;color:#fff;font-size:26px}
  .hero-arrows{margin-left:auto;font-size:22px;letter-spacing:10px}
  .contact-panel{position:absolute;left:26px;top:738px;width:620px;height:480px;background:var(--panel-bg);border:2px solid #e8e8e8}
  .contact-title{position:absolute;left:0;width:100%;top:36px;text-align:center;font-size:33px;font-weight:700;color:var(--phone-blue)}
  .contact-sub{position:absolute;left:0;width:100%;top:92px;text-align:center;font-size:31px;font-weight:300;color:var(--text-dark)}
  .field{position:absolute;left:56px;width:507px;height:62px;background:#fff;border:2px solid #dcdcdc;padding-left:22px;display:flex;align-items:center;font-size:19px;color:#777}
</style>
</head>
<body>
<div class="screen">
  <div class="status-bar">
    <div class="carrier">
      <span class="dots"><span class="dot"></span><span class="dot"></span><span class="dot"></span><span class="dot off"></span><span class="dot off"></span></span>
      <span>Operator</span>
      <svg width="24" height="18" viewBox="0 0 24 18"><path d="M2 6a14 14 0 0 1 20 0M5.5 9.5a9 9 0 0 1 13 0M9 13a4 4 0 0 1 6 0" stroke="#222" stroke-width="2.4" fill="none" stroke-linecap="round"/><circle cx="12" cy="16" r="1.6" fill="#222"/></svg>
    </div>
    <div class="time">11:27 AM</div>
    <div class="battery"><span>100 %</span><span class="battery-icon"></span></div>
  </div>

  <header class="site-header">
    <div class="brand">BRAMBLEWORTH</div>
    <div class="menu-button" aria-label="Menu">
      <svg width="38" height="32" viewBox="0 0 38 32"><rect y="2" width="38" height="5" fill="#fff"/><rect y="13.5" width="38" height="5" fill="#fff"/><rect y="25" width="38" height="5" fill="#fff"/></svg>
    </div>
  </header>

  <section class="call-block">
    <p class="call-text">Call <strong>Now</strong> for a Free Consultation</p>
    <a class="call-number" href="tel:5550104827">(555)010-4827</a>
    <a class="call-button" href="tel:5550104827" aria-label="Call">
      <svg width="50" height="50" viewBox="0 0 24 24"><path d="M6.6 10.8a15.1 15.1 0 0 0 6.6 6.6l2.2-2.2a1 1 0 0 1 1-.25 11.4 11.4 0 0 0 3.6.57 1 1 0 0 1 1 1V20a1 1 0 0 1-1 1A17 17 0 0 1 3 4a1 1 0 0 1 1-1h3.5a1 1 0 0 1 1 1c0 1.25.2 2.45.57 3.57a1 1 0 0 1-.25 1z" fill="#fff"/></svg>
    </a>
  </section>

  <section class="hero">
    <div class="hero-photo" role="img" aria-label="Aerial photograph of a coastal harbor with boats and a town"></div>
    <div class="hero-caption"><span>Newport Beach, California</span><span class="hero-arrows">‹ ›</span></div>
  </section>

  <section class="contact-panel">
    <h2 class="contact-title">How can we Help you?</h2>
    <p class="contact-sub">Talk To Us About Your Injury Now</p>
    <div class="field" style="top:169px">Name</div>
    <div class="field" style="top:254px">Email</div>
    <div class="field" style="top:342px">Phone</div>
    <div class="field" style="top:425px"></div>
  </section>
</div>
</body>
</html>
```